Bref créative
MOBILE ULTRASOUND BUSINESS
Professional
Nora K. Pellway Hussel
President and Director of Ultrasound
517 Thornbury Lane #2614
Millbrook Twp. PA. 15832
nora@keystonepulsescanworks.example
keystonepulsescanworks.example
We need business cards for my husband as well, all info will be the same except for his name is Gavin P. Hussel - Chief Operating Officer for title - and gavin@keystonepulsescanworks.example
vector logo file

```html
<!DOCTYPE html>
<html lang="en">
<head>
<meta charset="utf-8">
<title>BRQMOLVEX Stationery</title>
<link href="https://fonts.googleapis.com/css2?family=Montserrat:wght@400;600;800&display=swap" rel="stylesheet">
<style>
  :root{
    --bg-edge:#5d6a2c;
    --bg-mid:#c3cb97;
    --blue:#1b8fcb;
    --green:#5fb136;
    --ink:#2a2f33;
    --muted:#6b7378;
    --paper:#ffffff;
    --dark-card:#2b2d30;
    --caption:#f1f3e4;
  }
  *{box-sizing:border-box;margin:0;padding:0}
  html,body{width:1200px;height:382px;overflow:hidden}
  body{font-family:"Montserrat",Arial,sans-serif;color:var(--ink)}
  .canvas{position:relative;width:1200px;height:382px;overflow:hidden;
    background:radial-gradient(ellipse 70% 80% at 35% 45%,var(--bg-mid) 0%,#9aa65f 55%,var(--bg-edge) 100%)}
  .piece{position:absolute;background:var(--paper);box-shadow:0 2px 6px rgba(0,0,0,.35)}
  .brand{display:flex;align-items:center;gap:5px;white-space:nowrap}
  .brand-mark{width:12px;height:12px;background:var(--blue);flex:none}
  .brand-name{font-weight:800;color:var(--blue);font-size:11px;letter-spacing:.5px}
  .caption{position:absolute;font-size:6px;color:var(--caption);text-align:center;white-space:nowrap}

  .hero{position:absolute;left:60px;top:72px}
  .hero .brand-mark{width:40px;height:40px;background:var(--dark-card)}
  .hero .brand-name{font-size:24px;color:var(--dark-card);letter-spacing:1px}
  .hero-note{position:absolute;left:60px;top:132px;font-size:7px;color:var(--dark-card)}

  .card{width:145px;height:72px;padding:8px;overflow:hidden}
  .card .band{position:absolute;left:0;right:0;bottom:0;height:7px;
    background:linear-gradient(90deg,var(--blue) 70%,var(--green) 70%)}
  .card-front{display:flex;align-items:center;justify-content:center}
  .card-back .name{font-size:5.5px;font-weight:600;margin-top:5px;white-space:nowrap}
  .card-back p{font-size:4px;color:var(--muted);line-height:1.35;white-space:nowrap}
  .card.dark{background:var(--dark-card)}
  .card.dark .brand-name{color:#fff}
  .card.dark .name{color:#fff}
  .card.dark p{color:#c9cdd0}

  .letterhead{width:226px;height:312px;padding:14px}
  .letterhead .contact{position:absolute;left:128px;top:14px;font-size:4px;color:var(--muted);line-height:1.4;white-space:nowrap}
  .letterhead .foot{position:absolute;left:0;right:0;bottom:0;height:10px;
    background:linear-gradient(90deg,var(--blue) 75%,var(--green) 75%)}

  .envelope{width:316px;height:72px;overflow:hidden}
  .envelope svg{position:absolute;left:0;top:0;width:100%;height:100%}
  .envelope .seal{position:absolute;left:151px;top:22px;width:14px;height:14px;background:#fff}
  .envelope.front{width:186px;height:68px;padding:9px}
  .envelope.front .foot{position:absolute;left:0;right:0;bottom:0;height:7px;background:var(--blue)}
  .envelope.front .contact{font-size:4px;color:var(--muted);margin-top:4px;white-space:nowrap}
</style>
</head>
<body>
<main class="canvas">

  <div class="hero brand"><span class="brand-mark"></span><span class="brand-name">BRQMOLVEX</span></div>
  <div class="hero-note">Stationery Concept</div>

  <!-- business cards -->
  <div class="piece card card-front" style="left:19px;top:158px">
    <div class="brand"><span class="brand-mark"></span><span class="brand-name">BRQMOLVEX</span></div>
  </div>
  <div class="caption" style="left:19px;top:236px;width:145px">Front Light</div>

  <div class="piece card card-back" style="left:176px;top:158px">
    <div class="brand"><span class="brand-mark" style="width:8px;height:8px"></span><span class="brand-name" style="font-size:7px">BRQMOLVEX</span></div>
    <div class="name">Nora K. Pellway Hussel</div>
    <p>President and Director of Ultrasound</p>
    <p>517 Thornbury Lane #2614, Millbrook Twp. PA. 15832</p>
    <p>nora@keystonepulsescanworks.example</p>
    <p>keystonepulsescanworks.example</p>
    <div class="band"></div>
  </div>
  <div class="caption" style="left:176px;top:236px;width:145px">Back Light</div>

  <div class="piece card card-front dark" style="left:19px;top:252px">
    <div class="brand"><span class="brand-mark"></span><span class="brand-name">BRQMOLVEX</span></div>
  </div>
  <div class="caption" style="left:19px;top:330px;width:145px">Front Dark</div>

  <div class="piece card card-back dark" style="left:176px;top:252px">
    <div class="brand"><span class="brand-mark" style="width:8px;height:8px"></span><span class="brand-name" style="font-size:7px">BRQMOLVEX</span></div>
    <div class="name">Gavin P. Hussel</div>
    <p>Chief Operating Officer</p>
    <p>517 Thornbury Lane #2614, Millbrook Twp. PA. 15832</p>
    <p>gavin@keystonepulsescanworks.example</p>
    <p>keystonepulsescanworks.example</p>
    <div class="band"></div>
  </div>
  <div class="caption" style="left:176px;top:330px;width:145px">Back Dark</div>

  <!-- letterheads -->
  <div class="piece letterhead" style="left:343px;top:30px">
    <div class="brand"><span class="brand-mark"></span><span class="brand-name">BRQMOLVEX</span></div>
    <div class="contact">517 Thornbury Lane #2614<br>Millbrook Twp. PA. 15832<br>nora@keystonepulsescanworks.example</div>
    <div class="foot"></div>
  </div>
  <div class="caption" style="left:343px;top:350px;width:226px">Letterhead Page One</div>

  <div class="piece letterhead" style="left:600px;top:30px">
    <div class="brand"><span class="brand-mark"></span><span class="brand-name">BRQMOLVEX</span></div>
    <div class="contact">517 Thornbury Lane #2614<br>Millbrook Twp. PA. 15832<br>keystonepulsescanworks.example</div>
    <div class="foot"></div>
  </div>
  <div class="caption" style="left:600px;top:350px;width:226px">Letterhead Page Two</div>

  <!-- envelopes -->
  <div class="piece envelope" style="left:869px;top:72px">
    <svg viewBox="0 0 316 72" preserveAspectRatio="none">
      <defs><linearGradient id="flap-green" x1="0" y1="0" x2="0" y2="1">
        <stop offset="0" stop-color="#3f8f22"/><stop offset="1" stop-color="#7cc64f"/></linearGradient></defs>
      <polygon points="0,0 316,0 316,14 158,48 0,14" fill="url(#flap-green)"/>
      <polyline points="0,72 158,42 316,72" fill="none" stroke="#dfe3e6" stroke-width="1"/>
    </svg>
    <div class="seal"></div>
  </div>

  <div class="piece envelope" style="left:869px;top:152px">
    <svg viewBox="0 0 316 72" preserveAspectRatio="none">
      <defs><linearGradient id="flap-blue" x1="0" y1="0" x2="0" y2="1">
        <stop offset="0" stop-color="#136f9f"/><stop offset="1" stop-color="#3aa8dc"/></linearGradient></defs>
      <polygon points="0,0 316,0 316,14 158,48 0,14" fill="url(#flap-blue)"/>
      <polyline points="0,72 158,42 316,72" fill="none" stroke="#dfe3e6" stroke-width="1"/>
    </svg>
    <div class="seal"></div>
  </div>

  <div class="piece envelope" style="left:869px;top:234px;height:58px">
    <svg viewBox="0 0 316 58" preserveAspectRatio="none">
      <polygon points="0,0 316,0 158,30" fill="#f1f3f4" stroke="#dfe3e6"/>
    </svg>
  </div>

  <div class="piece envelope front" style="left:857px;top:282px">
    <div class="brand"><span class="brand-mark" style="width:9px;height:9px"></span><span class="brand-name" style="font-size:8px">BRQMOLVEX</span></div>
    <div class="contact">517 Thornbury Lane #2614, Millbrook Twp. PA. 15832</div>
    <div class="foot"></div>
  </div>

</main>
</body>
</html>
```